Business Cards for Volmar Pike, a law firm

We changed our firm's name from "Volmar & Pike LLP" to "Volmar Pike", we need to update our cards with a new design. We like the overall look of the back but the front side of the cards (see attached mockup) needs a refreshed look. I also attach our current logo so you can get rid of that LLP and &. We have a new address as well (not same as on mockup).

Target Market(s)

Clients of law firm

Industry/Entity Type

Law Firm

Contact Information for Business Card

Frontsides:

Lorenzo T. Volmar
Partner
Tel: (555) 710-2284 ext. 101
Fax: (555) 382-6419
Email: lvolmar@vplegal.example

Simon K. Pike
Partner
Tel: (555) 710-2284 ext. 102
Fax: (555) 382-6419
Email: simonpike@vplegal.example

Omar J. Benedek
Barrister
Tel: (555) 710-2284 ext. 104
Fax: (555) 382-6419
Email: obenedek@vplegal.example

The back side should be crimson red (see mockup) with the logo (please update it to remove the & and the LLP, you can modify it a bit to make it tasteful if need be). Our new address is

71 Marrowby Rd W, Suite 208
Toronto, ON M9X 3K5

After our address, please also include our website www.vplegal.example

Font styles to use
Sans Serif

Colors
ec2027
ffffff
000000

Requirements
Must have
• PLEASE NOTE: our firm's colour is more of a darker/crimson red, not a vibrant red.
• The front should have space for the lawyer's name, title, phone number (with extension), fax number, and email.
• If you're going to add those yourself, the info for the frontside is in the "Business Card Details" section (three lawyers that need their own cards).
Nice to have
• We like the backside of our current cards, just update it with our new address (one address now instead of 2), and a slightly modified logo (not a new logo altogether).
• The frontside should be refreshed with a better look (think minimalist, professional and modern), although still predominantly white-based background.
Should not have
• No scales of justice or other cheesy lawyer stereotype symbols! :-)

```html
<!DOCTYPE html>
<html lang="en">
<head>
<meta charset="utf-8">
<title>Volmar Pike — Card Front Contact Detail</title>
<link rel="stylesheet" href="https://fonts.googleapis.com/css2?family=Montserrat:wght@200;300&display=swap">
<style>
  :root {
    --paper: #ffffff;
    --ink: #000000;
    --crimson: #c41e1a;
    --panel: #f2f2f2;
    --leader: #c8c8c8;
    --guide: #5ff2f2;
  }
  html, body {
    margin: 0;
    padding: 0;
    width: 1200px;
    height: 2178px;
    overflow: hidden;
    background: var(--paper);
  }
  .card-detail {
    display: block;
    width: 1200px;
    height: 2178px;
  }
  .contact-line {
    font-family: "Montserrat", sans-serif;
    font-weight: 200;
    font-size: 460px;
    letter-spacing: 30px;
    fill: var(--ink);
  }
  .icon-fill { fill: var(--crimson); }
  .icon-cut { fill: var(--paper); }
  .icon-panel { fill: var(--panel); }
  .leader-line {
    stroke: var(--leader);
    stroke-width: 36;
    stroke-dasharray: 120 75;
    fill: none;
  }
  .guide { stroke: var(--guide); stroke-width: 3; }
</style>
</head>
<body>
<svg class="card-detail" viewBox="0 0 1200 2178" xmlns="http://www.w3.org/2000/svg">
  <!-- panel behind the fax and email icons -->
  <rect class="icon-panel" x="0" y="1050" width="315" height="660"/>

  <!-- phone icon -->
  <g class="icon-phone">
    <path class="icon-fill" d="M0 430 C60 500 120 545 175 560 L200 490 C215 455 250 460 255 510 L250 560 C240 590 190 590 150 580 C90 565 35 530 0 500 Z"/>
  </g>

  <!-- fax icon -->
  <g class="icon-fax">
    <rect class="icon-fill" x="0" y="825" width="150" height="150" rx="10"/>
    <rect class="icon-fill" x="0" y="960" width="255" height="240" rx="22"/>
    <rect class="icon-cut" x="0" y="975" width="170" height="18"/>
    <rect class="icon-cut" x="40" y="1110" width="130" height="24" rx="4"/>
    <rect class="icon-fill" x="45" y="1115" width="120" height="14"/>
  </g>

  <!-- email icon -->
  <g class="icon-email">
    <rect class="icon-fill" x="0" y="1410" width="255" height="330" rx="24"/>
    <path class="icon-cut" d="M0 1575 L45 1630 L255 1455 L255 1505 L45 1680 L0 1625 Z"/>
  </g>

  <!-- contact lines -->
  <text class="contact-line" x="480" y="591">(555) 710-2284 ext. 101</text>
  <text class="contact-line" x="480" y="1164">(555) 382-6419</text>
  <text class="contact-line" x="480" y="1746">lvolmar@vplegal.example</text>

  <!-- dashed leader -->
  <line class="leader-line" x1="45" y1="1125" x2="1200" y2="195"/>

  <!-- layout guides -->
  <line class="guide" x1="261" y1="0" x2="261" y2="2178"/>
  <line class="guide" x1="501" y1="0" x2="501" y2="2178"/>
  <line class="guide" x1="0" y1="594" x2="1200" y2="594"/>
  <line class="guide" x1="0" y1="1170" x2="1200" y2="1170"/>
  <line class="guide" x1="0" y1="1746" x2="1200" y2="1746"/>
</svg>
</body>
</html>
```